Awesome Dessert Baker needs Sticker Design

My wife is an incredible baker. She specializes in desserts and everyone that tastes her baked goods has told her to start selling them. She recently decided to go into business and just through word of mouth and her reputation she is already getting steady orders.

She is looking to have a sticker developed to put on her cake boxes and packaging.

She wants the following:
1. Colors to be used- hot pink, purple, white
2. Want a sleek, modern design and style incorporating following:
name: Whisked by Nora
tel: 646 382 1074
email: nora@whiskedbynora.example

**no old fashion baking references like rolling pins, aprons, ect.

We want the sticker to be very appealing and eye catching that will further promote her image and business.

Industry/Entity Type

Fashion

Requirements
Must have
• Must contain the following information:

Whisked by Nora
646 382 1074 (please make small and discreet)
nora@whiskedbynora.example (please make small and discreet)
Should not have
• **no old fashion baking references like rolling pins, aprons, ect.

```html
<!DOCTYPE html>
<html lang="en">
<head>
<meta charset="utf-8">
<title>Whisked by Nora – Sticker Set</title>
<link rel="stylesheet" href="https://fonts.googleapis.com/css2?family=Arimo:wght@400;700&display=swap">
<style>
  :root {
    --ring-grey: #bcbcbc;
    --mark-grey: #c4c4c4;
    --berry-purple: #5c2a88;
    --hot-pink: #e5007d;
    --paper-white: #ffffff;
    --canvas: #ffffff;
  }
  * { margin: 0; padding: 0; box-sizing: border-box; }
  html, body {
    width: 1200px;
    height: 427px;
    overflow: hidden;
    background: var(--canvas);
  }
  .sticker-sheet {
    position: relative;
    width: 1200px;
    height: 427px;
  }
  .sticker {
    position: absolute;
    top: 23px;
    width: 388px;
    height: 388px;
    border-radius: 50%;
    border: 17px solid var(--ring-grey);
    font-family: "Arimo", Arial, sans-serif;
  }
  .sticker--white  { left: 0;     background: var(--paper-white);  color: var(--berry-purple); }
  .sticker--purple { left: 406px; background: var(--berry-purple); color: var(--paper-white); }
  .sticker--pink   { left: 812px; background: var(--hot-pink);     color: var(--paper-white); }

  .brand-mark {
    position: absolute;
    left: 53px;
    top: 103px;
    width: 80px;
    height: 80px;
    border-radius: 50%;
    background: var(--paper-white);
  }
  .sticker--white .brand-mark { background: var(--mark-grey); }

  .brand-name {
    position: absolute;
    left: 103px;
    top: 45px;
    font-weight: 400;
    font-size: 44px;
    line-height: 48px;
    white-space: nowrap;
  }
  .brand-name__line { display: block; }
  .brand-name__line--second { padding-left: 30px; }

  .contact {
    position: absolute;
    left: 0;
    right: 0;
    top: 230px;
    text-align: center;
  }
  .contact__phone {
    display: block;
    font-weight: 700;
    font-size: 19px;
    letter-spacing: 0.3px;
  }
  .contact__email {
    display: block;
    margin-top: 9px;
    font-weight: 400;
    font-size: 19px;
  }
</style>
</head>
<body>
  <main class="sticker-sheet">
    <section class="sticker sticker--white" aria-label="White sticker">
      <span class="brand-mark" aria-hidden="true"></span>
      <h1 class="brand-name">
        <span class="brand-name__line">WHISKED</span>
        <span class="brand-name__line brand-name__line--second">by NORA</span>
      </h1>
      <p class="contact">
        <span class="contact__phone">646 382 1074</span>
        <span class="contact__email">nora@whiskedbynora.example</span>
      </p>
    </section>

    <section class="sticker sticker--purple" aria-label="Purple sticker">
      <span class="brand-mark" aria-hidden="true"></span>
      <h2 class="brand-name">
        <span class="brand-name__line">WHISKED</span>
        <span class="brand-name__line brand-name__line--second">by NORA</span>
      </h2>
      <p class="contact">
        <span class="contact__phone">646 382 1074</span>
        <span class="contact__email">nora@whiskedbynora.example</span>
      </p>
    </section>

    <section class="sticker sticker--pink" aria-label="Pink sticker">
      <span class="brand-mark" aria-hidden="true"></span>
      <h2 class="brand-name">
        <span class="brand-name__line">WHISKED</span>
        <span class="brand-name__line brand-name__line--second">by NORA</span>
      </h2>
      <p class="contact">
        <span class="contact__phone">646 382 1074</span>
        <span class="contact__email">nora@whiskedbynora.example</span>
      </p>
    </section>
  </main>
</body>
</html>
```